Marrowgate Auctions Business Cards Design Needed

I need a business card design that is modern looking - double sided (maybe just my logo on the back, but open to suggestions) - the overall design is up to you. I want it to be easy to read - not over the top flashy. I already have a company logo which I uploaded so that needs to be used. The colors of my logo are the colors I want on the card... so blue and gray (do need to match the logo colors).

Requirements
Must have
• Would like the card to be sleek, modern and easy to ready

```html
<!DOCTYPE html>
<html lang="en">
<head>
<meta charset="utf-8">
<title>Marrowgate Auctions – Business Cards</title>
<link href="https://fonts.googleapis.com/css2?family=Exo+2:wght@600;700&family=Montserrat:wght@500;700&family=Tinos:wght@700&display=swap" rel="stylesheet">
<style>
  :root {
    --brand-blue: #2a78c2;
    --brand-blue-dark: #1f62a3;
    --brand-gray: #55575b;
    --ink: #2b2b2b;
    --card-paper: #f4f4f4;
    --backdrop: #e6e7e9;
  }
  * { box-sizing: border-box; margin: 0; padding: 0; }
  html, body { width: 1200px; height: 800px; overflow: hidden; }
  body {
    background: var(--backdrop);
    display: flex;
    align-items: center;
    justify-content: center;
    gap: 40px;
  }
  .card {
    position: relative;
    width: 550px;
    height: 314px;
    background: var(--card-paper);
    box-shadow: 0 6px 18px rgba(0,0,0,.12);
    overflow: hidden;
  }
  .card svg { position: absolute; display: block; }

  /* Front */
  .front-top-chevron { top: 0; left: 200px; }
  .front-bottom-chevron { bottom: 0; left: 200px; }
  .front-brand {
    position: absolute;
    top: 92px; left: 0; right: 0;
    text-align: center;
    font-family: "Exo 2", sans-serif;
    font-weight: 700;
    font-size: 40px;
    line-height: 1.05;
    color: var(--brand-blue);
    letter-spacing: .5px;
  }
  .front-tagline {
    position: absolute;
    top: 186px; left: 93px;
    width: 364px; height: 46px;
    border: 1px solid #8a8a8a;
    display: flex; align-items: center; justify-content: center;
    font-family: "Tinos", serif;
    font-weight: 700;
    font-size: 18px;
    color: var(--ink);
  }

  /* Back */
  .back-ribbon { top: 0; left: 43px; }
  .ribbon-content {
    position: absolute;
    top: 52px; left: 43px; width: 148px;
    text-align: center;
    color: #fff;
  }
  .ribbon-brand {
    font-family: "Exo 2", sans-serif;
    font-weight: 700;
    font-size: 19px;
    line-height: 1.1;
  }
  .ribbon-tagline {
    margin-top: 12px;
    font-family: "Tinos", serif;
    font-weight: 700;
    font-size: 12px;
    line-height: 1.1;
  }
  .contact-block { position: absolute; top: 70px; left: 282px; }
  .holder-name {
    font-family: "Exo 2", sans-serif;
    font-weight: 700;
    font-size: 31px;
    line-height: 1;
    color: var(--brand-blue);
  }
  .holder-title {
    margin-top: 5px;
    font-family: "Montserrat", sans-serif;
    font-weight: 700;
    font-size: 10px;
    letter-spacing: 2.2px;
    color: var(--brand-gray);
  }
  .contact-list { list-style: none; margin-top: 38px; }
  .contact-item {
    display: flex; align-items: center; gap: 11px;
    height: 27px; margin-bottom: 6px;
    font-family: "Montserrat", sans-serif;
    font-weight: 500;
    font-size: 13px;
    color: var(--ink);
  }
  .contact-icon {
    position: static !important;
    width: 27px; height: 27px;
    background: var(--brand-blue);
  }
  .back-corner { bottom: 0; right: 20px; }
</style>
</head>
<body>

  <section class="card card-front" aria-label="Card front">
    <svg class="front-top-chevron" width="150" height="38" viewBox="0 0 150 38">
      <polygon points="0,0 150,0 110,26 75,37 40,26" fill="var(--brand-gray)"/>
      <polygon points="0,0 150,0 112,18 75,29 38,18" fill="var(--brand-blue)"/>
    </svg>

    <div class="front-brand">Marrowgate<br>Auctions</div>
    <div class="front-tagline">Improving Charity Auctions Nationwide</div>

    <svg class="front-bottom-chevron" width="150" height="38" viewBox="0 0 150 38">
      <polygon points="0,38 150,38 110,12 75,1 40,12" fill="var(--brand-gray)"/>
      <polygon points="0,38 150,38 112,20 75,9 38,20" fill="var(--brand-blue)"/>
    </svg>
  </section>

  <section class="card card-back" aria-label="Card back">
    <svg class="back-ribbon" width="148" height="210" viewBox="0 0 148 210">
      <polygon points="0,0 148,0 148,185 74,208 0,185" fill="var(--brand-gray)"/>
      <polygon points="0,0 148,0 148,172 74,195 0,172" fill="var(--brand-blue)"/>
    </svg>
    <div class="ribbon-content">
      <div class="ribbon-brand">Marrowgate<br>Auctions</div>
      <div class="ribbon-tagline">Improving Charity<br>Auctions Nationwide</div>
    </div>

    <div class="contact-block">
      <div class="holder-name">WES HARTLEY</div>
      <div class="holder-title">OWNER/PRESIDENT - AUCTIONEER</div>
      <ul class="contact-list">
        <li class="contact-item">
          <svg class="contact-icon" viewBox="0 0 27 27" aria-hidden="true">
            <rect width="27" height="27" fill="var(--brand-blue)"/>
            <path d="M9 7 l3 0 l1.5 4 l-2 1.5 a9 9 0 0 0 4 4 l1.5 -2 l4 1.5 l0 3 a2 2 0 0 1 -2 1.5 a13 13 0 0 1 -11.5 -11.5 a2 2 0 0 1 1.5 -2z" fill="#fff"/>
          </svg>
          555-014-7720
        </li>
        <li class="contact-item">
          <svg class="contact-icon" viewBox="0 0 27 27" aria-hidden="true">
            <rect width="27" height="27" fill="var(--brand-blue)"/>
            <rect x="7" y="9" width="13" height="9" fill="#fff"/>
            <polyline points="7,9 13.5,14 20,9" fill="none" stroke="var(--brand-blue)" stroke-width="1.3"/>
          </svg>
          info@marrowgate.com
        </li>
        <li class="contact-item">
          <svg class="contact-icon" viewBox="0 0 27 27" aria-hidden="true">
            <rect width="27" height="27" fill="var(--brand-blue)"/>
            <g fill="none" stroke="#fff" stroke-width="1.3">
              <circle cx="13.5" cy="13.5" r="6.5"/>
              <ellipse cx="13.5" cy="13.5" rx="3" ry="6.5"/>
              <line x1="7" y1="13.5" x2="20" y2="13.5"/>
              <line x1="8" y1="10" x2="19" y2="10"/>
              <line x1="8" y1="17" x2="19" y2="17"/>
            </g>
          </svg>
          http://bidrenewal.com
        </li>
      </ul>
    </div>

    <svg class="back-corner" width="126" height="36" viewBox="0 0 126 36">
      <polygon points="0,36 126,36 126,22 70,0 24,18" fill="var(--brand-gray)"/>
      <polygon points="24,18 70,0 126,22 126,27 70,6 32,20" fill="var(--brand-blue)"/>
    </svg>
  </section>

</body>
</html>
```